Investment Fee Schedule for Wealth Management Firm

We are a Chicago based firm that wants to illustrate our fee schedule for our Portfolios at different investment amounts. i.e. $50k & Under, $50k-$100k, $1-$250k, $250k-$750, $750-$1M etc. The idea is that the more money people invest they receive a volume discount. Each category has 4 portfolios with differing investment risk (Conservative, Balanced, Growth, Aggressive). Each portfolio is made up of Equities & Fixed Income shown as 20/80, 40/60/ 60/40 and 80/20. Need to name the Levels and make it easy for potential clients to understand. The attached is my sketch of how I came to price each model and might assist you in seeing how it works. May seem a bit complicated but really its just a variation on a theme. We need help communicating this in a marketing piece. We are easy to talk and work with. Hope to partner with you! Thank you for your consideration.

Update Brief 11/27/18
Some of the info I provided is not necessary and can be omitted. I would like the pie charts to be more traditional where the pie is broken down into solid color inside the circle.

Can we also take the table that you have at the top under the pie charts and expand on it? I believe that the top line should be a banner that says the companies being invested in. Under the 20/80 and 40/60 pies it would say the investment firms being used. Then the next line on this left side of the page in the same table would begin the pricing models starting with the word Level instead of tier.

Willow Ridge-Harbor Stone Capital-Brindle-Corvanta
Level 1A ($3.5M+) 1.06%
Level 1B ($2.5M-$3.5M) 1.16%
Level 1C ($1.5M-$2.5M) 1.21%
Level 1D ($$750k-$1.5M) 1.26%

On the right side under the 60/40 and 80/20 pie the banner would say:

Harbor Stone Capital-Steady Ledger Advisors-Brindle-Corvanta
Level 1A ($3.5M+) 1.08%
Level 1B ($2.5M-$3.5M) 1.18%
Level 1C ($1.5M-$2.5M) 1.23%
Level 1D ($$750k-$1.5M) 1.28%

Below these two tables would be two more tables maybe in a different shade to distinguish it from the Level one tables.

The banner again would show the investment firms being used under the two models 20/80 and 40/60.

Level 2 ($250k-$750k) 1.39%

Willow Ridge-Harbor Stone Capital-Corvanta
Level 3 ($100k-$250k) 1.45%

The next two Levels would have the banner run along the whole width of the page under all of the four models since they are using the same investment management firms.

Harbor Stone Capital-Corvanta
Level 4($50k-$100k) 1.50%

Corvanta-Fenmoor
ETF Choice (Under $50k) 1.25%

Harbor Stone Capital-Steady Ledger Advisors-Corvanta-Brindle
Level 2 ($250k-$750k) 1.41%

Harbor Stone Capital-Steady Ledger Advisors-Corvanta

I really tried to convey my vision but it's a bit hard to do so in words. I would be happy to email you a hand written copy of what I just said above.

Thank you!
Peter M.

Target Market(s)

Individual Investors

Industry/Entity Type

Financial Planning

Font styles to use
Serif
Sans Serif

Requirements
Must have
• Professional Appeal

```html
<!DOCTYPE html>
<html lang="en">
<head>
<meta charset="utf-8">
<title>Tier 1 Account Fee Schedule</title>
<link rel="stylesheet" href="https://fonts.googleapis.com/css2?family=Montserrat:wght@400;500;700;800&display=swap">
<style>
:root{
  --stage:#e9e9ec;
  --paper:#f3f3f3;
  --ink:#0b0b0d;
  --cyan:#19b4e6;
  --cyan-light:#4cc6e6;
  --navy-band:#1e4d63;
  --blue-head:#0d5fb0;
  --blue-row:#c5dceb;
  --blue-row-alt:#9fc7de;
  --blue-text:#0d5fb0;
  --red-head:#8c0a10;
  --red-row:#e4c8cc;
  --red-row-alt:#d29ea6;
  --red-text:#8c0a10;
  --text:#222;
}
*{box-sizing:border-box;margin:0;padding:0}
html,body{width:1200px;height:900px;overflow:hidden;background:var(--stage);font-family:"Montserrat",sans-serif}
.poster{position:absolute;left:319px;top:16px;width:492px;height:762px;background:var(--paper);transform:scale(1.135);transform-origin:0 0;overflow:hidden;box-shadow:0 4px 16px rgba(0,0,0,.18)}
.decor{position:absolute;left:0;top:0}
.price-range{position:absolute;right:6px;top:36px;color:var(--cyan);font-weight:800;font-size:24px;letter-spacing:-.3px}
.tier-title{position:absolute;left:46px;top:74px;color:#fff;font-weight:800;font-size:25px;letter-spacing:.2px}
.intro{position:absolute;left:36px;top:126px;width:456px;font-size:14.5px;line-height:18px;color:var(--text)}
.intro-lead{color:var(--cyan);font-weight:700}
.pie{position:absolute}
.pie text{font-family:"Montserrat",sans-serif;font-weight:800;font-size:15px;fill:#fff}
.fee-table{position:absolute;left:138px;width:215px;border-collapse:collapse;font-size:10px;color:#222}
.fee-table td,.fee-table th{height:19px;padding:0 0 0 11px;text-align:left;font-weight:500;border-right:2px solid var(--paper)}
.fee-table td:last-child,.fee-table th:last-child{border-right:0;padding-left:12px}
.fee-table th{color:#fff;font-weight:500;height:17px}
.fee-table th.pct{text-align:center;padding:0}
.fee-table .col-name{width:88px}
.fee-table .col-role{width:66px}
.fee-table.blue{top:325px}
.fee-table.blue th{background:var(--blue-head)}
.fee-table.blue td{background:var(--blue-row)}
.fee-table.blue tr.alt td{background:var(--blue-row-alt)}
.fee-table.blue tr.total td.hl{color:var(--blue-text)}
.fee-table.red{top:569px}
.fee-table.red th{background:var(--red-head)}
.fee-table.red td{background:var(--red-row)}
.fee-table.red tr.alt td{background:var(--red-row-alt)}
.fee-table.red tr.total td.hl{color:var(--red-text)}
.fee-table tr+tr td{border-top:2px solid var(--paper)}
</style>
</head>
<body>
<div class="poster">
  <svg class="decor" width="492" height="762" viewBox="0 0 492 762">
    <rect x="0" y="0" width="492" height="6" fill="#fff"/>
    <rect x="0" y="6" width="492" height="84" fill="var(--ink)"/>
    <rect x="0" y="86" width="492" height="6" fill="var(--cyan)"/>
    <polygon points="5,58 280,58 300,92 20,92" fill="#127fb0"/>
    <polygon points="20,86 297,86 316,117 38,117" fill="var(--cyan)"/>
    <polygon points="193,723 478,723 486,737 201,737" fill="var(--cyan-light)"/>
    <rect x="0" y="737" width="492" height="6" fill="var(--cyan)"/>
    <rect x="0" y="743" width="492" height="13" fill="var(--ink)"/>
    <polygon points="201,743 492,743 492,756 209,756" fill="var(--navy-band)"/>
    <rect x="0" y="756" width="492" height="6" fill="#fff"/>
  </svg>

  <div class="price-range">$250K-$750K</div>
  <h1 class="tier-title">TIER - 1 ACCOUNT</h1>

  <p class="intro"><span class="intro-lead">The companies being invested in.</span><br>Under the 20/80 and 40/60 pies it would say the investment firms being used.</p>

  <svg class="pie" style="left:64px;top:200px" width="170" height="110" viewBox="0 0 170 110" role="img" aria-label="Pie chart: 20% equities, 80% fixed income">
    <path d="M5 45 A80 42 0 0 0 165 45 L165 63 A80 42 0 0 1 5 63 Z" fill="#0a5bb5"/>
    <ellipse cx="85" cy="45" rx="80" ry="42" fill="#1a8ad6"/>
    <path d="M85 45 L38 11 A80 42 0 0 1 132 11 Z" fill="#3db54a"/>
    <text x="66" y="24">20%</text>
    <text x="65" y="66">80%</text>
  </svg>
  <svg class="pie" style="left:258px;top:200px" width="170" height="110" viewBox="0 0 170 110" role="img" aria-label="Pie chart: 40% equities, 60% fixed income">
    <path d="M5 45 A80 42 0 0 0 165 45 L165 63 A80 42 0 0 1 5 63 Z" fill="#0a5bb5"/>
    <ellipse cx="85" cy="45" rx="80" ry="42" fill="#1a8ad6"/>
    <path d="M85 45 L7.4 55.2 A80 42 0 0 1 136.4 12.8 Z" fill="#3db54a"/>
    <text x="46" y="33">40%</text>
    <text x="90" y="64">60%</text>
  </svg>

  <table class="fee-table blue">
    <tr><th colspan="2">Particular</th><th class="pct">%</th></tr>
    <tr><td class="col-name">Willow Ridge</td><td class="col-role">Platform</td><td>0.30%</td></tr>
    <tr class="alt"><td>Harbor Stone Capital</td><td>Mar..</td><td>0.24%</td></tr>
    <tr><td>Brindle</td><td>Rep..</td><td>0.85%</td></tr>
    <tr class="total"><td class="hl">Corvanta</td><td></td><td class="hl">1.39%</td></tr>
  </table>

  <svg class="pie" style="left:63px;top:441px" width="170" height="110" viewBox="0 0 170 110" role="img" aria-label="Pie chart: 40% equities, 60% fixed income">
    <path d="M5 45 A80 42 0 0 0 165 45 L165 63 A80 42 0 0 1 5 63 Z" fill="#7a0a0e"/>
    <path d="M5 45 A80 42 0 0 0 7.4 55.2 L7.4 73.2 A80 42 0 0 1 5 63 Z" fill="#c98410"/>
    <ellipse cx="85" cy="45" rx="80" ry="42" fill="#8c0a10"/>
    <path d="M85 45 L7.4 55.2 A80 42 0 0 1 136.4 12.8 Z" fill="#e39a12"/>
    <text x="46" y="33">40%</text>
    <text x="90" y="64">60%</text>
  </svg>
  <svg class="pie" style="left:258px;top:441px" width="170" height="110" viewBox="0 0 170 110" role="img" aria-label="Pie chart: 20% equities, 80% fixed income">
    <path d="M5 45 A80 42 0 0 0 165 45 L165 63 A80 42 0 0 1 5 63 Z" fill="#7a0a0e"/>
    <ellipse cx="85" cy="45" rx="80" ry="42" fill="#8c0a10"/>
    <path d="M85 45 L38 11 A80 42 0 0 1 132 11 Z" fill="#e39a12"/>
    <text x="66" y="24">20%</text>
    <text x="65" y="66">80%</text>
  </svg>

  <table class="fee-table red">
    <tr><th colspan="2">Particular</th><th class="pct">%</th></tr>
    <tr><td class="col-name">Willow Ridge</td><td class="col-role">Platform</td><td>0.30%</td></tr>
    <tr class="alt"><td>Harbor Stone Capital</td><td>Mar..</td><td>0.26%</td></tr>
    <tr><td>Brindle</td><td>Rep..</td><td>0.85%</td></tr>
    <tr class="total"><td class="hl">Corvanta</td><td></td><td class="hl">1.41%</td></tr>
  </table>
</div>
</body>
</html>
```